Redesign der Systemmails von motivhafen.de
Zielgruppe
Wir sind die Macher von motivhafen.de und wollen unsere Standardmails, die systemseitig verschickt werden, schöner und wertiger gestalten.
Aufgabenstellung
Wir sind der Meinung, dass unsere System-E-Mails ein Redesign nötig haben. Daher würden wir Dich bitten, uns Deinen Input zu geben. Die Mails sollen schlichter und moderner gestaltet werden. Folgende Elemente bedürfen aus unserer Sicht der Überarbeitung:
Schrift -> Aktuell verwenden wir Lucida Sans Unicode als Schrift für die Mails. Die Schrift passt aber nicht mehr so gut zur Seite. Auf der Seite verwenden wir inzwischen die Lato (leider keine Systemschrift).
Bitte schlage eine aus Deiner Sicht geeignete Systemschrift vor.
Buttonstyle -> Bitte einen frischen Buttonstyle vorschlagen
Schriftgröße und Farbe der Headline, des Fließtextes und des Footers -> Bitte harmonische Einteilung finden
Einen Screenshot einer aktuellen Mail ist anbei, außerdem einige Beispiele gelungener Mails anderer Unternehmen.
Die Datenlieferung sollte dann bitte als PSD und einer textlichen Beschreibung der Schriften, Schriftgrößen und Farbwerte erfolgen.
Bitte folgenden Text für die Gestaltung verwenden:
Hallo VORNAME NACHNAME,
Ihr Projekt 'BEISPIELPROJEKTTITEL' ist abgelaufen. Als nächstes sollten Sie ein Gewinner-Design bestimmen:
Button [Gewinner bestimmen]
Sie möchten noch Feinheiten am Design ändern lassen? Kein Problem: Finale Änderungen am Gewinnerdesign erledigt der Designer gerne im Rahmen der Datenübergabe. Küren Sie einfach Ihren Favoriten zum Gewinner und teilen Sie dem Designer Ihre Änderungswünsche in der Datenübergabe mit. Erst wenn Sie bestätigt haben, dass alle Daten mit den gewünschten Überarbeitungen vollständig übergeben wurden, wird das Preisgeld an den Designer transferiert.
Sie können sich zwischen Ihren Favoriten nicht entscheiden?
Kein Problem, nutzen Sie einfach unser praktisches Design-Voting und lassen Sie Familie, Freunde, Bekannte und Kollegen abstimmen. So sehen Sie, welches Design am besten ank..

```html
<!DOCTYPE html>
<html lang="de">
<head>
<meta charset="utf-8">
<title>motivhafen.de – Projekt abgelaufen</title>
<link href="https://fonts.googleapis.com/css2?family=Roboto:wght@400;500;700&display=swap" rel="stylesheet">
<style>
  :root {
    --brand-blue: #0b9de2;
    --brand-blue-dark: #0a86c8;
    --text: #555a5e;
    --text-dark: #444a4e;
    --sidebar-bg: #efefef;
    --page-bg: #ffffff;
    --card-bg: #ffffff;
    --trophy: #f5b800;
    --divider: #dddddd;
  }
  * { box-sizing: border-box; margin: 0; padding: 0; }
  html, body {
    width: 883px; height: 1200px; overflow: hidden;
    background: var(--page-bg);
    font-family: "Roboto", Arial, sans-serif;
    color: var(--text);
  }
  .mail {
    position: absolute; left: 62px; top: 68px;
    width: 754px; height: 1057px;
    background: var(--card-bg);
    box-shadow: 0 1px 5px rgba(0,0,0,.22);
  }
  .mail-header {
    position: absolute; left: 0; top: 0; width: 754px; height: 250px;
    background: linear-gradient(135deg, #1a9fe0 0%, #0c94d8 55%, #3aa9e4 100%);
  }
  .brand {
    position: absolute; left: 0; right: 0; top: 150px;
    display: flex; align-items: center; justify-content: center; gap: 12px;
    color: #fff; font-size: 37px; font-weight: 400; letter-spacing: .2px;
  }
  .brand-mark { width: 26px; height: 26px; border: 3px solid #fff; }
  .main { position: absolute; left: 46px; top: 250px; width: 397px; }
  .greeting {
    position: absolute; top: 75px; font-size: 20px; font-weight: 400;
    color: var(--text-dark); white-space: nowrap;
  }
  .greeting strong { color: var(--brand-blue); font-weight: 700; }
  .intro {
    position: absolute; top: 157px; left: -2px; width: 402px;
    font-size: 15px; line-height: 22px; text-align: center;
  }
  .intro strong { color: var(--brand-blue); font-weight: 700; }
  .cta {
    position: absolute; left: 32px; top: 237px; width: 331px; height: 62px;
    display: flex; border-radius: 3px; overflow: hidden;
    box-shadow: 0 2px 4px rgba(0,0,0,.25); text-decoration: none;
  }
  .cta-icon {
    width: 60px; background: #f3f3f3; display: flex; align-items: center; justify-content: center;
  }
  .cta-label {
    flex: 1; background: var(--brand-blue); color: #fff;
    font-size: 15.5px; font-weight: 700; letter-spacing: .8px;
    display: flex; align-items: center; justify-content: center; position: relative;
  }
  .cta-label::before {
    content: ""; position: absolute; left: 0; top: 50%; transform: translateY(-50%);
    border-top: 10px solid transparent; border-bottom: 10px solid transparent;
    border-left: 9px solid #f3f3f3;
  }
  .body-copy {
    position: absolute; width: 397px; font-size: 15px; line-height: 22px;
    text-align: justify; letter-spacing: .15px;
  }
  .copy-1 { top: 347px; }
  .copy-2 { top: 457px; }
  .copy-3 { top: 611px; }
  .sidebar {
    position: absolute; left: 503px; top: 250px; width: 251px; height: 807px;
    background: var(--sidebar-bg); text-align: center;
  }
  .sidebar-title {
    position: absolute; top: 60px; left: 0; right: 0;
    color: var(--brand-blue); font-size: 21px; font-weight: 700; line-height: 26px;
  }
  .sidebar-text {
    position: absolute; top: 150px; left: 0; right: 0; font-size: 15px; line-height: 22px;
  }
  .contact { position: absolute; left: 0; right: 0; }
  .contact-icon {
    width: 44px; height: 44px; border-radius: 50%; background: var(--brand-blue);
    margin: 0 auto; display: flex; align-items: center; justify-content: center;
  }
  .contact-value {
    margin-top: 16px; font-size: 15px; font-weight: 500; color: var(--text-dark); line-height: 22px;
  }
  .contact-mail { top: 229px; }
  .contact-phone { top: 344px; }
  .contact-hours { top: 459px; }
  .contact-hours .contact-value { margin-top: 12px; }
  .sidebar-divider {
    position: absolute; top: 602px; left: 27px; right: 27px; border-top: 1px solid var(--divider);
  }
  .imprint {
    position: absolute; top: 625px; left: 29px; right: 22px; text-align: left;
    font-size: 11px; line-height: 14.5px; color: var(--text);
  }
  .imprint strong { font-weight: 500; color: var(--text-dark); }
  .imprint p + p { margin-top: 14px; }
  .imprint a { color: var(--brand-blue); word-break: break-all; }
</style>
</head>
<body>
  <article class="mail">
    <header class="mail-header" role="img" aria-label="Blau getöntes Foto eines Arbeitsplatzes als Kopfbild">
      <div class="brand"><span class="brand-mark"></span><span>motivhafen.de</span></div>
    </header>

    <section class="main">
      <h1 class="greeting">HALLO <strong>VORNAME NACHNAME</strong>,</h1>
      <p class="intro">Ihr Projekt <strong>'BEISPIELPROJEKTTITEL'</strong> ist abgelaufen. Als nächstes sollten Sie ein Gewinner-Design bestimmen:</p>
      <a class="cta" href="#">
        <span class="cta-icon">
          <svg width="24" height="24" viewBox="0 0 24 24" aria-hidden="true">
            <path fill="var(--trophy)" d="M6 3h12v2h3v3a4 4 0 0 1-4 4h-.4A5 5 0 0 1 13 15v3h3v3H8v-3h3v-3a5 5 0 0 1-3.6-3H7a4 4 0 0 1-4-4V5h3V3zm-1 4v1a2 2 0 0 0 1.6 2A8 8 0 0 1 6 7H5zm13 0a8 8 0 0 1-.6 3A2 2 0 0 0 19 8V7h-1z"/>
            <path fill="#fff" d="M12 5.5l1 2 2.1.3-1.5 1.5.4 2.1L12 10.4l-2 1 .4-2.1-1.5-1.5 2.1-.3z"/>
          </svg>
        </span>
        <span class="cta-label">GEWINNER BESTIMMEN</span>
      </a>
      <p class="body-copy copy-1">Sie möchten noch Feinheiten am Design ändern lassen? Kein Problem: Finale Änderungen am Gewinnerdesign erledigt der Designer gerne im Rahmen der Datenübergabe.</p>
      <p class="body-copy copy-2">Küren Sie einfach Ihren Favoriten zum Gewinner und teilen Sie dem Designer Ihre Änderungswünsche in der Datenübergabe mit. Erst wenn Sie bestätigt haben, dass alle Daten mit den gewünschten Überarbeitungen vollständig übergeben wurden, wird das Preisgeld an den Designer transferiert.</p>
      <p class="body-copy copy-3">Sie können sich zwischen Ihren Favoriten nicht entscheiden? Kein Problem, nutzen Sie einfach unser praktisches Design-Voting und lassen Sie Familie, Freunde, Bekannte und Kollegen abstimmen. So sehen Sie, welches Design am besten ankommt.</p>
    </section>

    <aside class="sidebar">
      <h2 class="sidebar-title">HABEN SIE NOCH<br>FRAGEN?</h2>
      <p class="sidebar-text">Schreiben Sie uns eine Mail<br>oder rufen Sie uns an</p>

      <div class="contact contact-mail">
        <div class="contact-icon">
          <svg width="22" height="16" viewBox="0 0 22 16" aria-hidden="true">
            <rect x="0" y="0" width="22" height="16" rx="1.5" fill="#fff"/>
            <path d="M1 1.5l10 7 10-7" fill="none" stroke="var(--brand-blue)" stroke-width="1.8"/>
          </svg>
        </div>
        <p class="contact-value">support@motivhafen.de</p>
      </div>

      <div class="contact contact-phone">
        <div class="contact-icon">
          <svg width="24" height="24" viewBox="0 0 24 24" aria-hidden="true">
            <path fill="#fff" d="M6.6 10.8a15.1 15.1 0 0 0 6.6 6.6l2.2-2.2a1 1 0 0 1 1-.25 11.4 11.4 0 0 0 3.6.57 1 1 0 0 1 1 1V20a1 1 0 0 1-1 1A17 17 0 0 1 3 4a1 1 0 0 1 1-1h3.5a1 1 0 0 1 1 1c0 1.25.2 2.45.57 3.57a1 1 0 0 1-.25 1z"/>
          </svg>
        </div>
        <p class="contact-value">+49 (0)911-5550147</p>
      </div>

      <div class="contact contact-hours">
        <div class="contact-icon">
          <svg width="24" height="24" viewBox="0 0 24 24" aria-hidden="true">
            <path fill="#fff" d="M3 4h18v13H10l-4 4v-4H3z"/>
            <text x="12" y="14.5" text-anchor="middle" font-family="Roboto, Arial, sans-serif" font-size="10" font-weight="700" fill="var(--brand-blue)">?</text>
          </svg>
        </div>
        <p class="contact-value">Montag - Freitag<br>9.00 - 17.00 Uhr</p>
      </div>

      <div class="sidebar-divider"></div>

      <div class="imprint">
        <p><strong>motivhafen.de GmbH</strong><br>Hafenweg 8, 90402 Nürnberg, Deutschland<br>Geschäftsführer: Jonas Brehm und Lena Voigt, Amtsgericht Nürnberg: HRB 31576</p>
        <p>Sie können Ihre Maileinstellungen jederzeit ändern, indem Sie hier klicken: <a href="#">https://www.motivhafen.de/account.php?page=details</a>.</p>
      </div>
    </aside>
  </article>
</body>
</html>
```